Commercial and Residential landscape Flyer design

we would like a flyer to advertise our new landscaping division for our company. Phone Number 5184620371
email pinecrestgroundworkservices@mailorbit.net
address 7 Marlow Court Schenectady New York 12419
The design is up to you. ill attach some sample flyers in the file section
Target Market(s)
Residential and commercial properties
Industry/Entity Type
Landscape
Font styles to use
Sans Serif
Colors
Designer to choose colors to be used in the design.
Requirements
Must have
- Services offered
- Spring Cleanups
- Mulch installation
- Mowing
- Tree and shrub Maintenance
- Fall Cleanups
- Fully Insured
- Free Estimates
Nice to have
- See word file Please double check all grammar and spelling
- Feel free to use anything in the word file. Its totally up to you. It all doesn't need to be on it . would like to stick with the color scheme of the logo
Should not have
- there are no should not haves. We just want to get the word out that we have a landscape division

```html
<!DOCTYPE html>
<html lang="en">
<head>
<meta charset="UTF-8">
<title>Pinecrest Groundwork Services – Landscaping Flyer</title>
<link href="https://fonts.googleapis.com/css2?family=Montserrat:wght@400;500;600;700;800&display=swap" rel="stylesheet">
<style>
  :root {
    --brand-blue: #1580e3;
    --brand-blue-dark: #0c6cc8;
    --slate: #5d5e60;
    --slate-dark: #4e4f51;
    --ink: #1e1f21;
    --paper: #ffffff;
    --backdrop: #e4e6e8;
  }
  * { box-sizing: border-box; margin: 0; padding: 0; }
  html, body { width: 1200px; height: 1200px; overflow: hidden; }
  body {
    background: var(--backdrop);
    font-family: "Montserrat", sans-serif;
    color: var(--ink);
  }
  .flyer {
    position: absolute;
    left: 196px; top: 30px;
    width: 807px; height: 1140px;
    background: linear-gradient(160deg, #ffffff 0%, #f3f4f6 55%, #ffffff 100%);
    overflow: hidden;
    box-shadow: 0 6px 24px rgba(0,0,0,.12);
  }
  .header-band {
    position: absolute; left: 0; top: 0; width: 807px; height: 123px;
    background: var(--brand-blue);
  }
  .hero-photo {
    position: absolute; left: 0; top: 123px; width: 807px; height: 372px;
    background: linear-gradient(180deg, #4e6a78 0%, #2f5a34 40%, #3f8a2a 75%, #2e5f1f 100%);
  }
  .logo-badge {
    position: absolute; left: 288px; top: 40px; width: 231px; height: 142px;
    background: var(--brand-blue);
    border-radius: 0 0 116px 116px;
    display: flex; flex-direction: column; align-items: center; justify-content: center;
    color: var(--paper); text-align: center;
    padding-top: 8px;
  }
  .logo-badge .mark {
    width: 14px; height: 14px; background: var(--paper); border-radius: 50%; margin-bottom: 10px;
  }
  .logo-badge .name {
    font-weight: 800; font-size: 24px; letter-spacing: 0.5px; line-height: 1.05;
  }
  .logo-badge .sub {
    font-weight: 800; font-size: 10px; letter-spacing: 2.5px; margin-top: 5px;
  }
  .free-estimates {
    position: absolute; left: 145px; top: 454px; width: 340px; text-align: center;
    font-weight: 800; font-size: 27px; color: var(--paper); letter-spacing: 0.3px;
  }
  .title-band {
    position: absolute; left: 0; top: 495px; width: 807px; height: 97px;
    background: var(--slate);
    border-bottom: 12px solid var(--brand-blue);
    height: 109px;
  }
  .title-band .kicker {
    position: absolute; left: 43px; top: 10px;
    font-weight: 800; font-size: 26.5px; color: var(--paper); letter-spacing: 0.2px;
  }
  .title-band .headline {
    position: absolute; left: 40px; top: 34px;
    font-weight: 800; font-size: 63px; color: var(--paper); letter-spacing: 1px; line-height: 1;
  }
  .equipment-photo {
    position: absolute; left: 542px; top: 417px; width: 254px; height: 254px;
    border-radius: 50%; border: 7px solid var(--brand-blue);
    background: radial-gradient(circle at 55% 55%, #e07a22 0%, #c9651a 30%, #5b8d3a 60%, #3e6b2b 100%);
  }
  .content { position: absolute; left: 20px; width: 540px; }
  .section-heading {
    font-weight: 700; font-size: 17.5px; letter-spacing: 0.4px; color: var(--ink);
  }
  .body-copy {
    font-size: 12.7px; line-height: 16.3px; color: #2a2b2d; text-align: justify;
  }
  .intro { top: 632px; }
  .intro .body-copy { margin-top: 8px; }
  .services { top: 778px; }
  .services .body-copy { margin-top: 8px; text-align: left; }
  .service-list {
    list-style: none; display: grid; grid-template-columns: 234px 280px;
    grid-auto-flow: column; grid-template-rows: repeat(5, 17.6px);
    margin-top: 4px;
  }
  .service-list li {
    color: var(--brand-blue); font-weight: 600; font-size: 13.6px; line-height: 17.6px;
    padding-left: 18px; position: relative;
  }
  .service-list li::before {
    content: ""; position: absolute; left: 0; top: 5px; width: 11px; height: 8px;
    border-radius: 4px; background: var(--brand-blue);
  }
  .trees { top: 952px; }
  .trees .subhead {
    color: var(--brand-blue); font-weight: 500; font-size: 13.6px; margin-top: 10px;
  }
  .gallery {
    position: absolute; left: 567px; top: 725px; width: 220px; height: 136px;
    border-left: 6px solid var(--brand-blue); border-bottom: 6px solid var(--brand-blue);
    background: linear-gradient(135deg, #4f8f35 0%, #7bb34a 40%, #c46aa8 70%, #5c9a3c 100%);
  }
  .contact-box {
    position: absolute; left: 567px; top: 938px; width: 220px; height: 158px;
    background: var(--slate);
    color: var(--paper); text-align: center;
  }
  .contact-tab {
    position: absolute; left: 588px; top: 918px; width: 178px; height: 42px;
    background: var(--brand-blue);
    color: var(--paper); font-weight: 700; font-size: 22px;
    display: flex; align-items: center; justify-content: center;
  }
  .contact-box .address {
    margin-top: 42px; font-weight: 600; font-size: 12.7px; line-height: 16px; padding: 0 8px;
  }
  .contact-box .phone {
    margin-top: 8px; font-weight: 600; font-size: 19px;
    display: flex; align-items: center; justify-content: center; gap: 5px;
  }
  .contact-box .email {
    margin-top: 6px; font-size: 7.6px;
    display: flex; align-items: center; justify-content: center; gap: 3px;
  }
  .dot { display: inline-block; border-radius: 50%; background: var(--brand-blue); }
  .footer-band {
    position: absolute; left: 0; top: 1096px; width: 807px; height: 44px;
    background: var(--slate);
    color: var(--paper); font-size: 17.5px; letter-spacing: 0.3px;
    display: flex; align-items: center; justify-content: center;
  }
</style>
</head>
<body>
  <main class="flyer">
    <div class="header-band"></div>
    <div class="hero-photo" role="img" aria-label="Photo of a lit suburban house at dusk with a manicured lawn, landscaped beds and trees"></div>
    <div class="logo-badge">
      <span class="mark"></span>
      <span class="name">PINECREST</span>
      <span class="sub">GROUNDWORK SERVICES</span>
    </div>
    <div class="free-estimates">FREE ESTIMATES</div>

    <div class="title-band">
      <div class="kicker">COMMERCIAL AND RESIDENTIAL</div>
      <div class="headline">LANDSCAPING</div>
    </div>
    <div class="equipment-photo" role="img" aria-label="Photo of an orange stand-on commercial lawn mower on grass"></div>

    <section class="content intro">
      <h2 class="section-heading">IMPLEMENT A RESPONSIBLE LANDSCAPING DESIGN</h2>
      <p class="body-copy">At Pinecrest Groundwork Services, we are passionate about creating landscapes that are sustainable as well as beautiful. That's why we emphasize the use of xeriscape plants, healthy soils, and water-friendly designs in all landscapes we work on. When you rely on us for commercial and residential landscaping services, your business or yard will be healthy and your conscience clear.</p>
    </section>

    <section class="content services">
      <h2 class="section-heading">OUR SERVICES</h2>
      <p class="body-copy">Take comfort in knowing that we fully insured. Our lawn cleanup activities include:</p>
      <ul class="service-list">
        <li>Lawn mowing</li>
        <li>Sucker tree removal</li>
        <li>Mulch bed cleanup</li>
        <li>Fall cleanups</li>
        <li>Periodic cleanups</li>
        <li>Weed removal</li>
        <li>Leaf and debris rake up and removal</li>
        <li>Tree and shrub trimming</li>
        <li>Spring cleanups</li>
      </ul>
    </section>

    <section class="content trees">
      <h2 class="section-heading">MAINTAIN THE TREES &amp; SHRUBS ON YOUR PROPERTY</h2>
      <p class="subhead">Tree Trimming, Removal &amp; More</p>
      <p class="body-copy">If you have trees or shrubs that you need removed from your residential or commercial property then contact Pinecrest Groundwork Services today! Our team will be there in no time to cut those trees down and haul them away for you. We deal in removing small trees (under 20' in height).</p>
    </section>

    <div class="gallery" role="img" aria-label="Grid of six photos showing lawns, flower beds and landscaped garden borders"></div>

    <div class="contact-box">
      <p class="address"><span class="dot" style="width:7px;height:7px"></span> 7 Marlow Court Schenectady<br>New York 12419</p>
      <p class="phone">
        <svg width="14" height="14" viewBox="0 0 14 14" aria-hidden="true"><circle cx="7" cy="7" r="7" fill="#1580e3"/><path d="M4.6 3.6l1.3 1.6-.7.9c.5 1 1.3 1.8 2.3 2.3l.9-.7 1.6 1.3-.8 1.3C6.6 10.1 3.9 7.4 3.3 4.4z" fill="#fff"/></svg>
        5184620371
      </p>
      <p class="email"><span class="dot" style="width:7px;height:7px"></span> pinecrestgroundworkservices@mailorbit.net</p>
    </div>
    <div class="contact-tab">CONTACT US</div>

    <footer class="footer-band">pinecrestgroundworkservices@mailorbit.net</footer>
  </main>
</body>
</html>
```